Dr Halvey Brochure Plastic Surgeon

We need a three panel brochure for cosmetic surgery designed and ready for print. The brochure will have content and images on both sides. We attached the old brochure. The content needs to stay as on the attached pdf but please feel free to offer new designs. The color needs to match the brochure, which is a light blue and teal. The logo is attached. All images we want on the brochure are also attached.

We are looking for new fresh design but need to keep the content currently on the brochure.
Updates

The tri-fold brochure must be on 8.5" x 11" with an 1/8" bleed for printing.

Target Market(s)

Females ages 25 to 55 yrs old

Industry/Entity Type

Plastic Surgery

Font styles to use
Sans Serif

Colors
34a6d7

Requirements
Must have
• You must use the content provided from the attached brochure. Keep the same content on the current panels. Must use the same color scheme

```html
<!DOCTYPE html>
<html lang="en">
<head>
<meta charset="utf-8">
<title>Dr Halvey Tri-fold Brochure</title>
<link href="https://fonts.googleapis.com/css2?family=Questrial&display=swap" rel="stylesheet">
<style>
:root{
  --page:#e8e8e8;
  --teal-dark:#15777e;
  --teal:#1f989e;
  --teal-light:#33aeb3;
  --teal-text:#167f86;
  --body:#4a4a4a;
  --white:#ffffff;
}
*{box-sizing:border-box;margin:0;padding:0}
html,body{width:886px;height:1200px;overflow:hidden;background:var(--page);font-family:"Questrial",sans-serif}
.brochure{position:absolute;left:0;top:258px;width:886px;height:684px;background:linear-gradient(90deg,#f3f4f5,#fbfbfb 60%,#f1f2f3);box-shadow:0 6px 18px rgba(0,0,0,.25);overflow:hidden}
.panel{position:absolute;top:0;width:295.3px;height:684px}
.panel--cosmetic{left:0}
.panel--medical{left:295.3px}
.panel--profile{left:590.6px;background:var(--white)}
.header-bar{position:absolute;top:12px;left:0;height:31px;width:295px}
.header-bar svg{position:absolute;inset:0}
.header-bar h2{position:absolute;left:34px;top:5px;color:var(--white);font-weight:400;font-size:17px;letter-spacing:.3px;text-transform:uppercase}
.block{position:absolute;left:34px}
.block h3{color:var(--teal-text);font-weight:400;font-size:17px;line-height:20px;margin-bottom:3px}
.checklist{list-style:none}
.checklist li{font-size:11px;line-height:15.8px;color:var(--body);padding-left:15px;position:relative}
.checklist li::before{content:"✓";position:absolute;left:0;color:var(--teal);font-size:11px}
.band{position:absolute;left:0;top:449px;width:295.3px;height:176px}
.band--dark{background:var(--teal-dark)}
.band--mid{background:var(--teal)}
.band .checklist li{color:#e8f5f5}
.band .checklist li::before{color:#e8f5f5}
.band h3{color:var(--white)}
.footer{position:absolute;left:0;top:625px;width:295.3px;height:59px;background:var(--teal-light);color:var(--white);text-align:center;padding-top:8px}
.footer .phone{font-size:15px;line-height:22px}
.footer .web{font-size:13px;line-height:20px}
.icon{display:inline-block;vertical-align:-2px;margin-right:5px}
.medical-topics{position:absolute;left:34px;top:297px}
.medical-topics p{color:var(--teal-text);font-size:17px;line-height:24px}
.medical-topics .gap{margin-top:5px}
.contact{position:absolute;top:449px;left:0;width:295.3px;text-align:center;color:var(--white)}
.pin{position:absolute;left:133px;top:-16px}
.address{margin-top:34px;font-size:13.5px;line-height:17.5px}
.schedule{margin-top:17px;font-size:14px;line-height:20px;text-transform:uppercase}
.contact .num{font-size:15px;line-height:24px;font-weight:700;letter-spacing:.3px}
.brand{position:absolute;top:26px;left:0;width:295px;text-align:center}
.brand .name{font-size:19px;color:var(--teal-text);letter-spacing:.6px}
.brand .name .dot{display:inline-block;width:10px;height:10px;border-radius:50%;background:var(--teal-light);margin:0 6px 1px 2px}
.brand .tagline{font-size:7px;color:#7a8a8c;line-height:9px;letter-spacing:.2px;text-transform:uppercase;margin-top:2px}
.accent-bar{position:absolute;top:85px;left:24px;width:271px;height:10px;background:var(--teal)}
.photo{position:absolute;top:95px;left:24px;width:271px;height:354px;background:linear-gradient(160deg,#e9eef1 0%,#e4cdbf 45%,#d8b4a2 70%,#eef1f3 100%)}
.credentials{position:absolute;top:449px;left:0;width:295.3px;height:176px;background:var(--teal-dark);color:var(--white);text-align:center;padding-top:13px;font-size:12.5px;line-height:16px}
.credentials p{margin-bottom:8px}
.credentials p::before{content:"✓ "}
</style>
</head>
<body>
<main class="brochure">

  <section class="panel panel--cosmetic">
    <div class="header-bar">
      <svg width="295" height="31" viewBox="0 0 295 31"><polygon points="0,0 250,0 238,31 0,31" fill="#17808a"/><polygon points="256,0 295,0 295,31 244,31" fill="#33aeb3"/></svg>
      <h2>Cosmetic Services</h2>
    </div>
    <div class="block" style="top:52px">
      <h3>Surgery</h3>
      <ul class="checklist">
        <li>Co2 Bladeless Incisional</li><li>Blepharoplasty</li><li>Brow and Forehead Lifts</li><li>Midface Lifts</li>
      </ul>
    </div>
    <div class="block" style="top:146px">
      <h3>Lasers</h3>
      <ul class="checklist">
        <li>Erase Wrinkles and Fine Lines</li><li>Tighten Skin</li><li>Remove Stretch Marks</li><li>Minimize Vascular Lesions</li><li>Minimize Spider Veins</li><li>Improve Scars</li><li>Remove Skin Tags and Moles</li><li>Remove Dark Spots</li><li>Hair Removal</li><li>Improve Stress Incontinence</li><li>Vaginal Rejuvenation</li><li>Correct Vaginal Dryness and Itching</li>
      </ul>
    </div>
    <div class="block" style="top:367px">
      <h3>Advanced Laser Equipment</h3>
      <ul class="checklist">
        <li>Aurelis CO2 Laser</li><li>Aurelis Intima</li><li>Aurelis Q-Light</li>
      </ul>
    </div>
    <div class="band band--dark">
      <div class="block" style="top:15px">
        <h3>Injectables</h3>
        <ul class="checklist" style="margin-top:4px">
          <li>Removal of Wrinkles</li><li>Restoration of Facial Volume</li><li>TCA Medium Depth Chemical Peels</li><li>Minimally Invasive Neck Liposuction</li><li>Acne Scar Treatment</li><li>Tighten Neck</li><li>Remove Neck Fullness</li>
        </ul>
      </div>
    </div>
    <div class="footer">
      <div class="phone"><svg class="icon" width="13" height="13" viewBox="0 0 13 13"><circle cx="6.5" cy="6.5" r="5.8" fill="none" stroke="#fff" stroke-width="1.2"/><path d="M4.3 3.6l1.2 1.3-.6.9c.4.9 1.1 1.6 2 2l.9-.6 1.3 1.2-.8 1c-2.3-.3-4.4-2.4-4.7-4.7z" fill="#fff"/></svg>(555) 208-4471</div>
      <div class="web"><svg class="icon" width="10" height="10" viewBox="0 0 10 10"><circle cx="5" cy="5" r="4.3" fill="none" stroke="#fff"/><path d="M.7 5h8.6M5 .7c-2.2 2.6-2.2 6 0 8.6M5 .7c2.2 2.6 2.2 6 0 8.6" fill="none" stroke="#fff" stroke-width=".8"/></svg>www.HalveyMD.com</div>
    </div>
  </section>

  <section class="panel panel--medical">
    <div class="header-bar">
      <svg width="295" height="31" viewBox="0 0 295 31"><polygon points="0,0 250,0 238,31 0,31" fill="#17808a"/><polygon points="256,0 295,0 295,31 244,31" fill="#33aeb3"/></svg>
      <h2>Medical Services</h2>
    </div>
    <div class="block" style="top:52px">
      <h3>Eyelid Surgery</h3>
      <ul class="checklist">
        <li>Ptosis</li><li>Trauma</li><li>Tumors</li><li>Upper Blepharoplasty</li><li>Eyelid Malposition</li>
      </ul>
    </div>
    <div class="block" style="top:178px">
      <h3>Orbital Surgery</h3>
      <ul class="checklist">
        <li>Tumors</li><li>Trauma</li><li>Thyroid — Graves Disease</li><li>Enucleation/Evisceration</li>
      </ul>
    </div>
    <div class="medical-topics">
      <p>Tear Duct Surgery</p>
      <p class="gap">Brow &amp; Forehead Lifts</p>
      <p class="gap">Congenital/Pediatric<br>Disorders</p>
    </div>
    <div class="band band--mid"></div>
    <div class="contact">
      <svg class="pin" width="30" height="30" viewBox="0 0 30 30"><circle cx="15" cy="15" r="14" fill="#15777e" stroke="#fff" stroke-width="1.5"/><path d="M15 7.5a4.8 4.8 0 0 0-4.8 4.8c0 3.4 4.8 8.7 4.8 8.7s4.8-5.3 4.8-8.7A4.8 4.8 0 0 0 15 7.5z" fill="none" stroke="#fff" stroke-width="1.6"/><circle cx="15" cy="12.3" r="1.7" fill="#fff"/><path d="M11 22.5h8" stroke="#fff" stroke-width="1.4"/></svg>
      <p class="address">418 W. Lakeview Blvd<br>Suite 240<br>Lakeview TX 75999</p>
      <p class="schedule">Schedule a Consultation</p>
      <p class="num"><svg class="icon" width="13" height="13" viewBox="0 0 13 13"><circle cx="6.5" cy="6.5" r="5.8" fill="none" stroke="#fff" stroke-width="1.2"/><path d="M4.3 3.6l1.2 1.3-.6.9c.4.9 1.1 1.6 2 2l.9-.6 1.3 1.2-.8 1c-2.3-.3-4.4-2.4-4.7-4.7z" fill="#fff"/></svg>(555) 208-4490</p>
      <p class="num"><svg class="icon" width="13" height="12" viewBox="0 0 13 12"><rect x="3" y="0.5" width="7" height="3.5" fill="#fff"/><rect x="0.5" y="4" width="12" height="5" rx="1" fill="#fff"/><rect x="3" y="7.5" width="7" height="4" fill="#fff" stroke="#1f989e" stroke-width=".8"/></svg>(555) 316-7702</p>
    </div>
    <div class="footer">
      <div class="web" style="line-height:22px"><svg class="icon" width="12" height="9" viewBox="0 0 12 9"><rect x=".5" y=".5" width="11" height="8" fill="none" stroke="#fff"/><path d="M.5.5l5.5 4.5 5.5-4.5" fill="none" stroke="#fff"/></svg>renewedface@halveymd.com</div>
      <div class="web"><svg class="icon" width="10" height="10" viewBox="0 0 10 10"><circle cx="5" cy="5" r="4.3" fill="none" stroke="#fff"/><path d="M.7 5h8.6M5 .7c-2.2 2.6-2.2 6 0 8.6M5 .7c2.2 2.6 2.2 6 0 8.6" fill="none" stroke="#fff" stroke-width=".8"/></svg>www.HalveyMD.com</div>
    </div>
  </section>

  <section class="panel panel--profile">
    <div class="brand">
      <div class="name"><span class="dot"></span>JOLENE R. HALVEY MD</div>
      <div class="tagline">Oculofacial Aesthetic &amp; Reconstructive Plastic Surgery<br>Cosmetic Laser Surgery</div>
    </div>
    <div class="accent-bar"></div>
    <div class="photo" role="img" aria-label="Portrait photograph of a woman with a skin-peel effect on her cheek"></div>
    <div class="credentials">
      <p>Expert in Cosmetic Surgery</p>
      <p>Lakeview's only Board Certified<br>Cosmetic Laser Surgeon</p>
      <p>Triple Board Certified in Eyelid and<br>Facial Plastic Surgery</p>
      <p>Customized Care</p>
      <p>Feminine Approach</p>
    </div>
    <div class="footer">
      <div class="phone"><svg class="icon" width="13" height="13" viewBox="0 0 13 13"><circle cx="6.5" cy="6.5" r="5.8" fill="none" stroke="#fff" stroke-width="1.2"/><path d="M4.3 3.6l1.2 1.3-.6.9c.4.9 1.1 1.6 2 2l.9-.6 1.3 1.2-.8 1c-2.3-.3-4.4-2.4-4.7-4.7z" fill="#fff"/></svg>(555) 208-4471</div>
      <div class="web"><svg class="icon" width="10" height="10" viewBox="0 0 10 10"><circle cx="5" cy="5" r="4.3" fill="none" stroke="#fff"/><path d="M.7 5h8.6M5 .7c-2.2 2.6-2.2 6 0 8.6M5 .7c2.2 2.6 2.2 6 0 8.6" fill="none" stroke="#fff" stroke-width=".8"/></svg>www.HalveyMD.com</div>
    </div>
  </section>

</main>
</body>
</html>
```